Speakwright election of District 71 Club Growth Director.

This is a tri-fold brochure. I have a basic layout from last years election but would like to add some detail and punch to the campaign brochure. I have a sample from last year. I've also included a sample of a brochure with some depth and personality. The design should communicate that I am a transformational leader who has a solid foundation in helping others to build a better Speakwright experience. If you have the winning design I will need business cards, post cards, and a poster.

Target Market(s)

Speakwright leaders with in Georgia. 25 yrs to 64 yrs = 80% of membership; 51% are female, over 75% have at least a Bachelor's degree or higher; 40% are specialist and 24% managers; 27% earn $100,000 or more - 41% earn $75,000 per year.

Industry/Entity Type

Non-Profit

Font styles to use
Sans Serif

Requirements
Must have
• Professional look. Playing off my experience as a residential contractor. Nickname is "iron boot" Morlow.
Nice to have
• larger font
Should not have
• Can not be hard to read

```html
<!DOCTYPE html>
<html lang="en">
<head>
<meta charset="utf-8">
<title>Michelle Morlow – Club Growth Director Brochure</title>
<link href="https://fonts.googleapis.com/css2?family=Bebas+Neue&family=Fira+Sans:wght@400;500&display=swap" rel="stylesheet">
<style>
  :root {
    --safety-yellow: #fff200;
    --stripe-yellow: #e3c02e;
    --title-yellow: #f7e81a;
    --panel-dark: #1c1c1c;
    --panel-mid: #4a4a4a;
    --concrete-light: #e9e9e7;
    --concrete-mid: #c9c9c6;
    --ink: #111111;
    --paper: #ffffff;
    --crop: #111111;
  }
  * { margin: 0; padding: 0; box-sizing: border-box; }
  html, body { width: 1200px; height: 915px; overflow: hidden; }
  body {
    background: var(--safety-yellow);
    position: relative;
    font-family: "Fira Sans", "Helvetica Neue", Arial, sans-serif;
  }
  .crop-mark { position: absolute; width: 2px; height: 54px; background: var(--crop); }
  .crop-mark--top { top: 30px; }
  .crop-mark--bottom { top: 832px; }
  .crop-mark--fold1 { left: 418px; }
  .crop-mark--fold2 { left: 759px; }

  .brochure {
    position: absolute; left: 78px; top: 94px; width: 1023px; height: 724px;
    box-shadow: 6px 8px 10px rgba(0,0,0,0.45);
    overflow: hidden;
  }
  .inside-spread {
    position: absolute; left: 0; top: 0; width: 681px; height: 724px;
    background: radial-gradient(ellipse 55% 50% at 55% 40%, var(--panel-mid), var(--panel-dark) 85%);
  }
  .cover-panel {
    position: absolute; left: 681px; top: 0; width: 342px; height: 724px;
    overflow: hidden;
    background: radial-gradient(ellipse at 40% 30%, var(--concrete-light), var(--concrete-mid) 90%);
  }

  .condensed { display: inline-block; transform: scaleX(0.82); transform-origin: left center; white-space: nowrap; }
  .condensed--center { transform-origin: center center; }

  .body-copy {
    position: absolute; width: 260px; color: var(--paper);
    font-size: 14.6px; line-height: 17.6px; text-align: justify;
  }
  .body-copy p { margin-bottom: 17.6px; }
  .body-copy ul { margin: 0 0 17.6px 24px; }
  .body-copy--left { left: 37px; top: 109px; }
  .body-copy--left li::marker { color: var(--title-yellow); }
  .body-copy--middle { left: 381px; top: 57px; }
  .body-copy--middle li::marker { color: var(--paper); }

  .section-banner { position: absolute; left: 0; top: 46px; width: 304px; height: 48px; }
  .section-banner__text {
    position: absolute; left: 37px; top: 55px;
    font-family: "Bebas Neue", Impact, sans-serif; font-size: 32px; line-height: 32px;
    font-weight: 400; color: var(--ink);
  }

  .vote-block {
    position: absolute; left: 361px; top: 478px; width: 300px; text-align: center;
    color: var(--title-yellow);
  }
  .vote-block__headline {
    font-family: "Bebas Neue", Impact, sans-serif; font-size: 40px; line-height: 36px;
  }
  .vote-block__detail { font-size: 14.6px; line-height: 17.6px; }

  .hazard-stripes { position: absolute; left: 0; top: 632px; }

  .cover-title {
    position: absolute; left: 29px; top: 0; width: 313px;
    font-family: "Bebas Neue", Impact, sans-serif; line-height: 1; font-weight: 400;
  }
  .cover-title > * { position: absolute; left: 0; }
  .cover-title__kicker, .cover-title__role {
    color: var(--title-yellow); text-shadow: 3px 3px 5px rgba(0,0,0,0.55);
  }
  .cover-title__kicker { top: 86px; font-size: 42px; }
  .cover-title__name { color: var(--ink); font-size: 76px; font-weight: 400; }
  .cover-title__name--first { top: 126px; }
  .cover-title__name--last { top: 196px; }
  .cover-title__role { top: 274px; font-size: 43px; }

  .candidate-portrait {
    position: absolute; left: 0; top: 350px; width: 300px; height: 374px;
    background: linear-gradient(to bottom, #e4e2de 0%, #c9a993 35%, #5a3d2c 60%, #efefed 75%, #f5f5f3 100%);
  }
  .cover-stripe { position: absolute; left: 0; top: 0; }
</style>
</head>
<body>
  <div class="crop-mark crop-mark--top crop-mark--fold1"></div>
  <div class="crop-mark crop-mark--top crop-mark--fold2"></div>
  <div class="crop-mark crop-mark--bottom crop-mark--fold1"></div>
  <div class="crop-mark crop-mark--bottom crop-mark--fold2"></div>

  <div class="brochure">
    <section class="inside-spread">
      <svg class="section-banner" width="304" height="48" viewBox="0 0 304 48">
        <polygon points="0,6 304,0 284,46 0,44" fill="var(--title-yellow)"/>
      </svg>
      <h2 class="section-banner__text"><span class="condensed">Meet Michelle Morlow</span></h2>

      <div class="body-copy body-copy--left">
        <p>Quas nominavi appetere sea te. Novum impedit nonumes ne vel, nec at solet aliquam.</p>
        <p>Mundi aliquip scribentur ut vim, cu usu ignota iuvaret honestatis. Et ius argumentum disputando, cum ut electram suscipiantur, an illud decore mel.</p>
        <ul>
          <li>Sed et mucius minimum, quas nostrum ea ius.</li>
          <li>Ad similique elaboraret pri, mel volutpat liberavisse ex, at duo eleifend postulant incorrupte.</li>
          <li>Ex tractatos iudicabit scribentur per, sed agam autem at.</li>
          <li>Nec ne justo munere tritani, ludus eleifend ut nec.</li>
        </ul>
        <p>Mea ex omnis voluptatibus, sea at nihil integre referrentur. Solum partem ea eum, eam inermis iudi-cabit ne. Qui te illud vitae philoso-phia.</p>
        <p>At fugit iisque sea, no vix nonumes ponderum contentiones.</p>
      </div>

      <div class="body-copy body-copy--middle">
        <p>Lorem ipsum dolor sit amet, sit et sale tacimates, mel ad regione admodum dissentiet. Quas nominavi appetere sea te. Novum impedit nonumes ne vel, nec at solet aliquam.</p>
        <ul>
          <li>Mundi aliquip scribentur ut vim, cu usu ignota iuvaret honestatis.</li>
          <li>Et ius argumentum disputando, cum ut electram suscipiantur, an illud decore mel.</li>
          <li>Sed et mucius minimum, quas nostrum ea ius.</li>
          <li>Ad similique elaboraret pri, mel volutpat liberavisse ex, at duo eleifend postulant incorrupte.</li>
          <li>Ex tractatos iudicabit scribentur per, sed agam autem at.</li>
          <li>Nec ne justo munere tritani, ludus eleifend ut nec.</li>
          <li>Nec ne justo munere tritani, ludus eleifend ut nec.</li>
        </ul>
      </div>

      <div class="vote-block">
        <div class="vote-block__headline">
          <div>Vote</div>
          <div><span class="condensed condensed--center">Michelle Morlow, DTM</span></div>
        </div>
        <div class="vote-block__detail">Club Growth Director<br>Michelle@MorlowVotes.org<br>678-555-0142</div>
      </div>

      <svg class="hazard-stripes" width="681" height="92" viewBox="0 0 681 92">
        <g fill="var(--stripe-yellow)">
          <polygon points="8,0 53,2 33,92 -14,92"/>
          <polygon points="97,0 142,2 122,92 75,92"/>
          <polygon points="186,0 231,2 211,92 164,92"/>
          <polygon points="275,0 320,2 300,92 253,92"/>
          <polygon points="364,0 409,2 389,92 342,92"/>
          <polygon points="453,0 498,2 478,92 431,92"/>
          <polygon points="542,0 587,2 567,92 520,92"/>
          <polygon points="631,0 676,2 656,92 609,92"/>
        </g>
      </svg>
    </section>

    <section class="cover-panel">
      <div class="cover-title">
        <div class="cover-title__kicker"><span class="condensed">Please Vote For</span></div>
        <h1 class="cover-title__name cover-title__name--first"><span class="condensed">Michelle</span></h1>
        <div class="cover-title__name cover-title__name--last"><span class="condensed">Morlow</span></div>
        <div class="cover-title__role"><span class="condensed">Club Growth Director</span></div>
      </div>
      <div class="candidate-portrait" role="img" aria-label="Portrait photo of candidate Michelle Morlow wearing a white hard hat and white jacket"></div>
      <svg class="cover-stripe" width="342" height="724" viewBox="0 0 342 724">
        <polygon points="297,632 342,632 342,724 277,724" fill="var(--stripe-yellow)"/>
      </svg>
    </section>
  </div>
</body>
</html>
```